Boutique Real Estate Brokerage looking for business card, letterhead and envelope design

We are looking for a cohesive design for our business cards, letterhead and envelopes and that mirrors our high-end homes and clientele. Cedar & Vale is being launched and designed for the marketplace of tomorrow. We grew from the #1 team in our community into a full-service firm that is going to revolutionize the traditional real estate model.

We understand that it’s more important than ever to help our clients and partners adapt to behavioral and market changes being driven by generational shifts and technological advances in society, and by combining traditional brokerage services with innovative production and marketing capabilities, we know how to do that better than anyone else.

Requirements
Must have
• business card, letterhead and envelope design - attached logo.

```html
<!DOCTYPE html>
<html lang="en">
<head>
<meta charset="utf-8">
<title>Cedar &amp; Vale — Stationery</title>
<link href="https://fonts.googleapis.com/css2?family=Lato:wght@400;700;900&display=swap" rel="stylesheet">
<style>
:root{
  --navy:#24185a;
  --gold:#c68f45;
  --ink:#3a3a3a;
  --muted:#8c8c8c;
  --paper:#ffffff;
  --bg:#e8e8eb;
}
*{box-sizing:border-box;margin:0;padding:0}
html,body{width:1180px;height:1200px;overflow:hidden}
body{background:var(--bg);font-family:"Lato",sans-serif;color:var(--ink);position:relative}

.sheet{position:absolute;background:var(--paper);overflow:hidden;box-shadow:0 6px 18px rgba(0,0,0,.18)}
/* plain navy edge band */
.sheet::after{content:"";position:absolute;top:0;right:0;bottom:0;width:var(--band,30px);background:var(--navy)}
/* plain gold base rule */
.sheet::before{content:"";position:absolute;left:0;bottom:0;right:var(--band,30px);height:var(--rule,8px);background:var(--gold)}

.brand{position:absolute;display:flex;align-items:center;gap:7px;font-weight:900;color:var(--navy);letter-spacing:.02em;white-space:nowrap}
.brand-dot{background:var(--gold);display:block}
.web{color:var(--gold);font-weight:400;letter-spacing:.01em;white-space:nowrap}
.web strong{font-weight:700}

/* letterhead */
.letterhead{left:40px;top:40px;width:440px;height:622px;--band:26px;--rule:8px}
.letterhead .brand{left:52px;top:54px;font-size:17px}
.letterhead .brand-dot{width:14px;height:14px}
.letter-body{position:absolute;left:52px;top:198px;width:338px;font-size:8.2px;line-height:1.45;color:var(--muted);text-align:justify;letter-spacing:.03em}
.letter-body p{margin-bottom:11px}
.footer-contact{position:absolute;left:52px;bottom:42px;font-size:8.6px;line-height:1.5;color:var(--ink)}
.footer-contact b{color:var(--gold);font-weight:700}
.letterhead .web{position:absolute;right:50px;bottom:42px;font-size:11px}

/* business cards */
.card{left:520px;width:560px;height:300px;--band:38px;--rule:10px}
.card-front{top:40px}
.card-back{top:380px}
.card-front .brand{left:60px;top:42px;font-size:20px}
.card-front .brand-dot{width:16px;height:16px}
.holder{position:absolute;left:60px;top:118px}
.holder h2{font-size:18px;font-weight:900;color:var(--navy)}
.holder p{font-size:10.5px;color:var(--navy);margin-top:2px}
.card-contact{position:absolute;left:60px;top:220px;font-size:11.5px;line-height:1.5;color:var(--navy)}
.card-contact b{color:var(--gold)}
.card-contact span{margin-left:20px}
.card-back .web{position:absolute;left:0;right:38px;top:138px;text-align:center;font-size:20px}

/* envelopes */
.envelope-dl{left:40px;top:700px;width:700px;height:350px;--band:40px;--rule:10px}
.envelope-dl .brand{left:70px;top:58px;font-size:18px}
.envelope-dl .brand-dot{width:15px;height:15px}
.contacts{position:absolute;list-style:none;font-size:8.5px;color:var(--navy)}
.contacts li{display:flex;align-items:center;gap:8px;margin-bottom:8px;white-space:nowrap}
.contacts svg{flex:none}
.envelope-dl .contacts{left:70px;top:190px}
.envelope-dl .web{position:absolute;left:70px;top:272px;font-size:15px}
.window{position:absolute;border:1px solid #cfcfd4;border-radius:6px;background:linear-gradient(135deg,#f7f7f9,#ececf0)}
.envelope-dl .window{left:330px;top:175px;width:290px;height:135px}

.envelope-c4{left:790px;top:700px;width:350px;height:470px;--band:30px;--rule:9px}
.envelope-c4 .brand{left:34px;top:62px;font-size:15px}
.envelope-c4 .brand-dot{width:12px;height:12px}
.envelope-c4 .contacts{left:40px;top:350px;font-size:7.5px}
.envelope-c4 .web{position:absolute;left:40px;top:418px;font-size:12px}
.envelope-c4 .window{left:214px;top:360px;width:96px;height:52px;border-radius:8px}
</style>
</head>
<body>

<svg width="0" height="0" style="position:absolute">
  <defs>
    <symbol id="ico-phone" viewBox="0 0 12 12"><circle cx="6" cy="6" r="6" fill="var(--gold)"/><path d="M4 3.2l1 1.4-.6.7c.4.9 1 1.5 1.9 1.9l.7-.6 1.4 1-.6 1.2C5.8 8.6 3.4 6.2 3.2 4z" fill="#fff"/></symbol>
    <symbol id="ico-mail" viewBox="0 0 12 12"><circle cx="6" cy="6" r="6" fill="var(--gold)"/><rect x="3" y="4" width="6" height="4.2" fill="none" stroke="#fff" stroke-width=".8"/><path d="M3 4l3 2.3L9 4" fill="none" stroke="#fff" stroke-width=".8"/></symbol>
    <symbol id="ico-pin" viewBox="0 0 12 12"><circle cx="6" cy="6" r="6" fill="var(--gold)"/><path d="M6 9.6C4.4 7.6 3.6 6.3 3.6 5.2a2.4 2.4 0 0 1 4.8 0C8.4 6.3 7.6 7.6 6 9.6z" fill="#fff"/><circle cx="6" cy="5.2" r=".9" fill="var(--gold)"/></symbol>
  </defs>
</svg>

<section class="sheet letterhead">
  <div class="brand"><span class="brand-dot"></span>CEDAR &amp; VALE</div>
  <div class="letter-body">
    <p>Lorem ipsum dolor sit amet, consectetur adipiscing elit. Fusce dignissim pretium consectetur. Curabitur tempor posuere massa in varius. Pellentesque viverra nibh eu vehicula mattis. Nullam porta facilisis justo, a feugiat dolor sodales sed. Vestibulum neque nisi, elementum tincidunt metus sit amet, egestas bibendum enim. Aenean a blandit elit, vel rutrum mi. Nunc dapibus turpis sed massa aliquet tincidunt.</p>
    <p>Pellentesque id neque ligula. Nullam posuere, ligula a mattis posuere, lacus nisl adipiscing nunc, eu congue justo est ut diam. Nam quam nibh, dignissim non consequat in, semper eget purus. Nulla arcu sapien, viverra vitae metus tempor, congue ornare diam.</p>
    <p>Pellentesque vel nibh tempus, ullamcorper tortor sed, bibendum augue. Phasellus sollicitudin justo et quam aliquam sollicitudin. Sed eget nibh mollis, mattis sem et, viverra nulla.</p>
    <p>Pellentesque vel nibh tempus, ullamcorper tortor sed, bibendum augue. Phasellus sollicitudin justo et quam aliquam sollicitudin. Sed eget nibh mollis, mattis sem et, viverra nulla.</p>
  </div>
  <div class="footer-contact">18 Linden Row, Fairhaven 40213<br><b>T.</b> +1 555 0142 7781 &nbsp;&nbsp; <b>M.</b> +1 555 0142 7781</div>
  <div class="web">www.<strong>cedarandvale</strong>.com</div>
</section>

<section class="sheet card card-front">
  <div class="brand"><span class="brand-dot"></span>CEDAR &amp; VALE</div>
  <div class="holder"><h2>MISTER ADLER</h2><p>Procurement Project Lead</p></div>
  <div class="card-contact">18 Linden Row, Fairhaven 40213<br><b>T.</b> +1 555 0142 7781<span><b>M.</b> +1 555 0142 7781</span></div>
</section>

<section class="sheet card card-back">
  <div class="web">www.<strong>cedarandvale</strong>.com</div>
</section>

<section class="sheet envelope-dl">
  <div class="brand"><span class="brand-dot"></span>CEDAR &amp; VALE</div>
  <ul class="contacts">
    <li><svg width="13" height="13"><use href="#ico-phone"/></svg>+1 555 0142 7781 / +1 555 0142 7781</li>
    <li><svg width="13" height="13"><use href="#ico-mail"/></svg>hello@cedarandvale.com</li>
    <li><svg width="13" height="13"><use href="#ico-pin"/></svg>18 Linden Row, Fairhaven 40213</li>
  </ul>
  <div class="web">www.<strong>cedarandvale</strong>.com</div>
  <div class="window"></div>
</section>

<section class="sheet envelope-c4">
  <div class="brand"><span class="brand-dot"></span>CEDAR &amp; VALE</div>
  <ul class="contacts">
    <li><svg width="11" height="11"><use href="#ico-phone"/></svg>+1 555 0142 7781 / +1 555 0142 7781</li>
    <li><svg width="11" height="11"><use href="#ico-mail"/></svg>hello@cedarandvale.com</li>
    <li><svg width="11" height="11"><use href="#ico-pin"/></svg>18 Linden Row, Fairhaven 40213</li>
  </ul>
  <div class="web">www.<strong>cedarandvale</strong>.com</div>
  <div class="window"></div>
</section>

</body>
</html>
```